Restaurant Posters

Looking for two posters to be created for restaurant promos - see below for details:

Design #1 -
Want to highlight two main specials we offer - first is Tuesday BOGO Burgers (with purchase of two beverages), second is on Wednesday's we offer $0.75 Wings (includes traditional and boneless) and $2 off IPA's

Then at the bottom smaller would like to call out two less important offers - first is $2 off Nebraska Beers on Mondays, and the second is 1/2 off 19.2oz Crowlers on Thursdays

Design #2 -
Looking to create a sign up for our e-club and receive a free appetizer upon sign up, free burger on your birthday week, and access to exclusive deals and email offers

See attached for supporting docs you may use - don't have to but feel free to get creative with these. Would like the designs to be simple, and follow our brand look and feel as much as possible. Our website is not a good indication of our brand - I would go more off of our logos, and our menu design.

Need extra days to review

```html
<!DOCTYPE html>
<html lang="en">
<head>
<meta charset="utf-8">
<title>Prairie Tap House – Restaurant Posters</title>
<link href="https://fonts.googleapis.com/css2?family=Alfa+Slab+One&family=Big+Shoulders+Inline+Display:wght@700&family=Montserrat:wght@500;700;800&family=Fjalla+One&family=Bebas+Neue&family=Nunito:wght@600;700&display=swap" rel="stylesheet">
<style>
  :root{
    --backdrop:#efe9e1;
    --charcoal:#2b2b2b;
    --charcoal-dark:#1e1e1e;
    --gold:#f7b801;
    --red:#e01e1e;
    --white:#ffffff;
    --brown-dark:#1c140d;
    --brown-mid:#4a3523;
    --parchment:#dcc59c;
    --parchment-light:#eadbbb;
    --ink:#2a221b;
    --signup-red:#e1260f;
  }
  *{box-sizing:border-box;margin:0;padding:0}
  html,body{width:1200px;height:851px;overflow:hidden;background:var(--backdrop)}
  .canvas{position:relative;width:1200px;height:851px}
  .poster{position:absolute;top:81px;width:488px;height:689px;overflow:hidden}

  /* ---------- Poster 1: weekly specials ---------- */
  .specials{left:72px;background:radial-gradient(ellipse at 50% 40%,#3a3a3a 0%,var(--charcoal) 50%,var(--charcoal-dark) 100%)}
  .specials .day{position:absolute;top:62px;left:0;width:100%;text-align:center;font-family:"Alfa Slab One",serif;font-size:46px;font-weight:400;color:var(--white);letter-spacing:1px;line-height:1}
  .specials .headline{position:absolute;top:120px;left:57px;width:382px;height:104px;overflow:visible}
  .specials .headline text{font-family:"Big Shoulders Inline Display",sans-serif;font-weight:700;font-size:136px;fill:var(--gold)}
  .specials .condition{position:absolute;top:232px;left:0;width:100%;text-align:center;font-family:"Montserrat",sans-serif;font-weight:500;font-size:15px;color:var(--white);line-height:18px}
  .specials .hero-photo{position:absolute;left:58px;top:282px;width:392px;height:262px;border-radius:46% 46% 18% 18%/60% 60% 20% 20%;background:radial-gradient(ellipse at 45% 45%,#f0e2c8 0%,#d99a4a 35%,#9b5a22 70%,#5a3415 100%)}
  .badge{position:absolute;border-radius:50%;background:var(--red);color:var(--white);text-align:center;display:flex;flex-direction:column;justify-content:center;align-items:center;box-shadow:0 0 0 2px var(--red),inset 0 0 0 3px rgba(255,255,255,.25)}
  .badge-wings{left:343px;top:254px;width:104px;height:104px}
  .badge-wings .price{font-family:"Alfa Slab One",serif;font-size:25px;line-height:1}
  .badge-wings .item{font-family:"Montserrat",sans-serif;font-weight:700;font-size:21px;line-height:1.05}
  .badge-wings .note{font-family:"Montserrat",sans-serif;font-weight:800;font-size:5px;line-height:1.2;margin-top:2px}
  .badge-ipa{left:26px;top:516px;width:100px;height:100px;z-index:2}
  .badge-ipa .price{font-family:"Alfa Slab One",serif;font-size:36px;line-height:1}
  .badge-ipa .item{font-family:"Montserrat",sans-serif;font-weight:800;font-size:11px}
  .callout-bar{position:absolute;left:117px;top:557px;width:335px;height:41px;background:var(--gold);display:flex;align-items:center;padding-left:24px;font-family:"Fjalla One",sans-serif;font-size:19px;color:var(--charcoal-dark);letter-spacing:.2px;white-space:nowrap}
  .brand-lockup{position:absolute;left:34px;top:626px;width:150px;font-family:"Fjalla One",sans-serif;color:var(--white);font-size:21px;line-height:1.05;letter-spacing:2px;text-align:center;text-transform:uppercase}
  .divider{position:absolute;left:193px;top:618px;width:2px;height:58px;background:var(--gold)}
  .minor-offers{position:absolute;left:200px;top:628px;list-style:none;font-family:"Montserrat",sans-serif;font-weight:800;font-size:10.6px;color:var(--white);line-height:22px;white-space:nowrap}
  .minor-offers .num{color:var(--gold);font-size:14px;margin-right:2px}

  /* ---------- Poster 2: e-club ---------- */
  .eclub{left:625px;background:radial-gradient(ellipse at 50% 50%,var(--brown-mid) 0%,#2e2116 55%,var(--brown-dark) 100%)}
  .torn-band{position:absolute;left:0;top:40px;width:100%;height:157px;background:linear-gradient(180deg,var(--parchment-light),var(--parchment));clip-path:polygon(0 8%,6% 4%,12% 7%,20% 2%,28% 6%,36% 1%,44% 5%,52% 0,60% 4%,68% 1%,76% 6%,84% 2%,92% 5%,100% 3%,100% 90%,95% 86%,90% 94%,84% 88%,78% 96%,70% 89%,62% 97%,55% 90%,48% 100%,40% 92%,33% 98%,25% 90%,18% 97%,10% 89%,4% 96%,0 90%)}
  .torn-band .line-one{position:absolute;top:22px;left:0;width:100%;text-align:center;font-family:"Bebas Neue",sans-serif;font-weight:400;font-size:60px;color:var(--red);line-height:1;letter-spacing:1px}
  .torn-band .line-two{position:absolute;top:78px;left:0;width:100%;text-align:center;font-family:"Bebas Neue",sans-serif;font-weight:400;font-size:72px;color:var(--ink);line-height:1;letter-spacing:2px}
  .eclub .hero-photo{position:absolute;left:23px;top:234px;width:416px;height:231px;border-radius:48% 48% 12% 12%/70% 70% 14% 14%;background:radial-gradient(ellipse at 50% 50%,#f3ead6 0%,#d9a45d 38%,#7a4a22 72%,#3b2410 100%)}
  .signup-tag{position:absolute;left:149px;top:491px;width:183px;height:35px;background:var(--signup-red);color:var(--white);font-family:"Montserrat",sans-serif;font-weight:800;font-style:italic;font-size:31px;line-height:35px;text-align:center}
  .benefit{position:absolute;font-family:"Nunito",sans-serif;font-weight:700;font-size:16.5px;color:var(--white);line-height:19.5px;text-align:center}
  .benefit-left{left:22px;top:544px;width:170px}
  .benefit-right{left:192px;top:541px;width:162px}
  .benefit-right .highlight{color:var(--gold);font-size:21px;line-height:26px;display:block}
  .club-mark{position:absolute;left:369px;top:512px;width:92px;height:92px;border:2px solid var(--white);border-radius:50%;display:flex;align-items:center;justify-content:center;text-align:center;font-family:"Nunito",sans-serif;font-weight:700;font-size:11px;color:var(--white);line-height:1.2}
  .flames{position:absolute;left:0;bottom:0;width:100%;height:90px;background:linear-gradient(180deg,rgba(255,140,20,0) 0%,rgba(235,120,20,.55) 45%,#c8621a 75%,#8a3a10 100%)}
</style>
</head>
<body>
<main class="canvas">

  <section class="poster specials" aria-label="Weekly specials poster">
    <h1 class="day">TUESDAY</h1>
    <svg class="headline" viewBox="0 0 382 104" role="heading" aria-level="2" aria-label="BOGO BURGERS">
      <text x="0" y="99" textLength="382" lengthAdjust="spacingAndGlyphs">BOGO BURGERS</text>
    </svg>
    <p class="condition">WITH PURCHASE OF TWO BEVERAGES</p>
    <div class="hero-photo" role="img" aria-label="Photo of a loaded cheeseburger with crispy toppings and sauce, tots on the side"></div>
    <div class="badge badge-wings">
      <span class="price">$0.75</span>
      <span class="item">WINGS</span>
      <span class="note">INCLUDES TRADITIONAL<br>AND BONELESS</span>
    </div>
    <div class="badge badge-ipa">
      <span class="price">$2</span>
      <span class="item">OFF IPA'S</span>
    </div>
    <div class="callout-bar">CALL OUT TWO LESS IMPORTANT OFFERS</div>
    <div class="brand-lockup">Prairie Tap House</div>
    <span class="divider"></span>
    <ol class="minor-offers">
      <li><span class="num">1.</span>$2 OFF NEBRASKA BEERS ON MONDAYS</li>
      <li><span class="num">2.</span>1/2 OFF 19.2OZ CROWLERS ON THURSDAYS</li>
    </ol>
  </section>

  <section class="poster eclub" aria-label="E-club sign up poster">
    <div class="torn-band">
      <h1 class="line-one">FREE BURGER ON YOUR</h1>
      <h2 class="line-two">BIRTHDAY WEEK</h2>
    </div>
    <div class="hero-photo" role="img" aria-label="Photo of a mac and cheese topped burger on a brioche bun"></div>
    <div class="flames" role="img" aria-label="Flames along the bottom edge"></div>
    <div class="signup-tag">SIGN UP</div>
    <p class="benefit benefit-left">our e-club and receive a freeappe-tizer upon sign up</p>
    <p class="benefit benefit-right">access to exclusive deals and <span class="highlight">Email offers</span></p>
    <div class="club-mark">Prairie<br>Tap House</div>
  </section>

</main>
</body>
</html>
```